Would like a design for lawn signs I will be using to advertise with. Attached are three images. One is the jpeg version of our logo to use in creating and editing the design. The other two are mock ups of our current style of tshirt and business card design. I would like the finished product to look similar in style to the mock ups. The actual color of our logo in the jpeg picture is outdated coloring. I would like the logo to be the color of the logo in the mock up tshirt version and the business card design.
The signs I will be using are white in color and 18"x24" white lawn signs, so I would like the logo to appear like the logo in the grey tshirt design, where it is black and orange. As for the text coloring I would like it to be black as well.
The only things I want included on the text of the sign design is:
Phone: 913-472-6081
Email: birchvaleyard@quillnet.com
Mowing
Fertilization
Aeration
Bed & tree maintenance
and more.

```html
<!DOCTYPE html>
<html lang="en">
<head>
<meta charset="utf-8">
<title>Birchvale Yard – Lawn Sign</title>
<link href="https://fonts.googleapis.com/css2?family=Roboto+Condensed:wght@700&display=swap" rel="stylesheet">
<style>
  :root {
    --orange: #ee5f24;
    --black: #000000;
    --white: #ffffff;
  }
  html, body {
    margin: 0;
    padding: 0;
    width: 1200px;
    height: 900px;
    overflow: hidden;
    background: var(--orange);
  }
  .sign {
    position: relative;
    width: 1200px;
    height: 900px;
    background: var(--orange);
    font-family: "Roboto Condensed", "Arial Narrow", sans-serif;
    font-weight: 700;
    color: var(--white);
  }
  .sign-panel {
    position: absolute;
    left: 25px;
    top: 25px;
    width: 1150px;
    height: 850px;
    background: var(--black);
  }
  .brand {
    position: absolute;
    left: 0;
    top: 200px;
    width: 1200px;
    display: flex;
    align-items: center;
    justify-content: center;
    gap: 28px;
  }
  .brand-dot {
    width: 70px;
    height: 70px;
    border-radius: 50%;
    background: var(--orange);
  }
  .brand-name {
    font-size: 96px;
    line-height: 1;
    text-transform: uppercase;
    letter-spacing: 2px;
  }
  .contact-icon {
    position: absolute;
  }
  .icon-phone { left: 125px; top: 518px; }
  .icon-mail { left: 123px; top: 655px; }
  .phone {
    position: absolute;
    left: 290px;
    top: 500px;
    font-size: 124px;
    line-height: 1;
    letter-spacing: 1px;
  }
  .email {
    position: absolute;
    left: 290px;
    top: 643px;
    font-size: 64px;
    line-height: 1;
  }
  .services {
    position: absolute;
    right: 60px;
    top: 750px;
    width: 1100px;
    text-align: right;
    font-size: 30px;
    line-height: 40px;
  }
  .services .sep {
    color: var(--orange);
    font-size: 18px;
    margin: 0 12px;
    vertical-align: middle;
  }
</style>
</head>
<body>
  <main class="sign">
    <div class="sign-panel"></div>

    <div class="brand">
      <span class="brand-dot"></span>
      <span class="brand-name">Birchvale Yard</span>
    </div>

    <svg class="contact-icon icon-phone" width="64" height="84" viewBox="0 0 64 84" aria-hidden="true">
      <path d="M6 4 V72 L14 80 H58 V12 H6" fill="none" stroke="var(--orange)" stroke-width="7" stroke-linejoin="miter"/>
      <rect x="20" y="28" width="24" height="24" fill="none" stroke="var(--orange)" stroke-width="6"/>
    </svg>
    <div class="phone">913-472-6081</div>

    <svg class="contact-icon icon-mail" width="84" height="56" viewBox="0 0 84 56" aria-hidden="true">
      <rect x="3.5" y="3.5" width="77" height="49" fill="none" stroke="var(--orange)" stroke-width="7"/>
      <path d="M4 5 L42 34 L80 5 M4 52 L32 27 M80 52 L52 27" fill="none" stroke="var(--orange)" stroke-width="6"/>
    </svg>
    <div class="email">birchvaleyard@quillnet.com</div>

    <div class="services">
      Mowing<span class="sep">★</span>Fertilization<span class="sep">★</span>Aeration<span class="sep">★</span>Bed &amp; Tree maintenance<span class="sep">★</span>Snow removal<br>and more..
    </div>
  </main>
</body>
</html>
```